Digital Menu Board for Restaurant

I want a digital menu board for our new restaurant. I have provided the sample of what I kind of want.
This is to be on a 55 inch tv so it needs to be the correct aspect ratio of 4:5

Font styles to use
Serif
Sans Serif

Colors
f59296
f04a50
ec1f27
ffffff
fffef7
fbed22
ffc214
0592cd
e5519f

Requirements
Must have
• fun, maybe something moving? bright colors on a darker background so it's easy to read or dark font on a light background.

```html
<!DOCTYPE html>
<html lang="en">
<head>
<meta charset="utf-8">
<title>Sandy Cove Menu Board</title>
<link href="https://fonts.googleapis.com/css2?family=Cabin:wght@700&family=PT+Sans:wght@700&family=Open+Sans:ital,wght@1,700&display=swap" rel="stylesheet">
<style>
  :root {
    --page: #ffffff;
    --barn-red: #c8141d;
    --barn-line: #5a0a0e;
    --panel: rgba(66, 48, 42, 0.92);
    --frame: #fffef7;
    --ink-dark: #3a2823;
    --item: #fffef7;
    --desc: #ffc214;
    --rule: #f0a020;
    --green: #5d9c3c;
    --red: #ec1f27;
    --blue: #4d5aa8;
    --pink: #e5519f;
    --teal: #3e9c93;
    --brand: #f26a2a;
  }
  * { box-sizing: border-box; margin: 0; padding: 0; }
  html, body { width: 1200px; height: 1200px; overflow: hidden; background: var(--page); }
  .board {
    position: absolute; left: 0; top: 263px; width: 1200px; height: 673px;
    background-color: var(--barn-red);
    background-image:
      linear-gradient(90deg, transparent 0 148px, var(--barn-line) 148px 152px, transparent 152px),
      linear-gradient(90deg, transparent 0 404px, var(--barn-line) 404px 408px, transparent 408px),
      linear-gradient(90deg, transparent 0 620px, var(--barn-line) 620px 624px, transparent 624px),
      linear-gradient(90deg, transparent 0 870px, var(--barn-line) 870px 874px, transparent 874px),
      linear-gradient(90deg, transparent 0 1100px, var(--barn-line) 1100px 1104px, transparent 1104px);
    overflow: hidden;
  }
  .menu-col {
    position: absolute; top: 35px;
    background: var(--panel); border: 3px solid var(--frame);
    display: flex; flex-direction: column;
  }
  .col-head {
    height: 116px; display: flex; align-items: center; justify-content: center;
    text-align: center; font-family: 'Cabin', sans-serif; font-weight: 700;
    color: var(--ink-dark); font-size: 35px; line-height: 1.02; letter-spacing: 0.5px;
  }
  .col-head.small { font-size: 28px; }
  .green-shore { left: 22px; width: 202px; height: 611px; }
  .green-shore .col-head { background: var(--green); }
  .between-buns { left: 245px; width: 239px; height: 611px; }
  .between-buns .col-head { background: var(--red); }
  .shakes { left: 504px; width: 247px; height: 611px; }
  .shakes .col-head { background: var(--blue); }
  .kids { left: 774px; width: 190px; height: 348px; }
  .kids .col-head { background: var(--pink); }
  .sides { left: 986px; width: 190px; height: 348px; }
  .sides .col-head { background: var(--teal); }
  .items { padding: 12px 9px; display: flex; flex-direction: column; }
  .item-name {
    font-family: 'PT Sans', sans-serif; font-weight: 700; color: var(--item);
    font-size: 15px; text-transform: uppercase; text-align: center; line-height: 1.3;
  }
  .item-desc {
    font-family: 'Open Sans', sans-serif; font-style: italic; font-weight: 700;
    color: var(--desc); font-size: 12.2px; line-height: 1.3; text-align: justify;
  }
  .green-shore .items { gap: 0; }
  .green-shore .entry { margin-bottom: 36px; }
  .green-shore .entry + .entry { border-top: 1.5px dashed var(--rule); padding-top: 14px; }
  .between-buns .entry { margin-bottom: 10px; }
  .list .item-name { padding: 6px 0; }
  .list .item-name + .item-name { border-top: 1.5px dashed var(--rule); }
  .kids .item-name { font-size: 13px; padding: 8px 0; }
  .kids .item-name + .item-name { border-top: none; }
  .sides .item-name { padding: 7px 0; }
  .drinks {
    border-top: 3px solid var(--rule); margin-top: 4px; padding-top: 8px;
    font-family: 'PT Sans', sans-serif; font-weight: 700; color: var(--desc);
    font-size: 15px; text-transform: uppercase; text-align: center; line-height: 1.4;
  }
  .brand {
    position: absolute; left: 820px; top: 505px; width: 350px;
    display: flex; align-items: center; justify-content: center; gap: 14px;
    font-family: 'PT Sans', sans-serif; font-weight: 700; color: var(--brand);
    font-size: 58px; line-height: 1;
  }
  .brand-dot { width: 30px; height: 30px; border-radius: 50%; background: var(--brand); flex: none; }
</style>
</head>
<body>
<main class="board">
  <section class="menu-col green-shore">
    <h2 class="col-head">GREEN<br>SHORE</h2>
    <div class="items">
      <div class="entry"><p class="item-name">North Beach Salad</p><p class="item-desc">Pulled pork and black beans on a bed of Romaine, Tomato and Onion with Sweet and sour Raspberry pineapple sauce.</p></div>
      <div class="entry"><p class="item-name">West Side Salad</p><p class="item-desc">Pulled pork and black beans on a bed of Romaine, Tomato and Onion with Sweet and sour Raspberry pineapple sauce.</p></div>
      <div class="entry"><p class="item-name">East Side Salad</p><p class="item-desc">Pulled pork and black beans on a bed of Romaine, Tomato and Onion with Sweet and sour Raspberry pineapple sauce.</p></div>
    </div>
  </section>

  <section class="menu-col between-buns">
    <h2 class="col-head">BETWEEN<br>BUNS</h2>
    <div class="items">
      <div class="entry"><p class="item-name">1st Point Pulled Pork</p><p class="item-desc">Pulled pork and black beans on a bed of Romaine, Tomato and Onion with Sweet and sour Raspberry pineapple sauce.</p></div>
      <div class="entry"><p class="item-name">2nd Point Pulled Pork</p><p class="item-desc">Pulled pork and black beans on a bed of Romaine, Tomato and Onion with Sweet</p></div>
      <div class="entry"><p class="item-name">Spiniker Point Burger</p><p class="item-desc">Pulled pork and black beans on a bed of Romaine, Tomato and Onion with Sweet and</p></div>
      <div class="entry"><p class="item-name">The Rock Burger</p><p class="item-desc">Pulled pork and black beans on a bed of Romaine, Tomato and Onion with Sweet and</p></div>
      <div class="entry"><p class="item-name">Rainbow Cove Sandwich</p><p class="item-desc">Pulled pork and black beans on a bed of Romaine, Tomato and Onion with Sweet and</p></div>
    </div>
  </section>

  <section class="menu-col shakes">
    <h2 class="col-head">SHAKES<br>N DRINKS</h2>
    <div class="items list">
      <p class="item-name">Milo's Signature<br>Raspberry Jammin Shake</p>
      <p class="item-name">Raspberry Cookie<br>Crumble Shake</p>
      <p class="item-name">Raspberry Hazel Cream<br>Bomb Shake</p>
      <p class="item-name">Raspberry Beaching<br>Shake (Pina Colada)</p>
      <p class="item-name">Raspberry Brownie<br>Shake</p>
      <p class="item-name">Caramel Shake</p>
      <p class="item-name">Chocolate Shake</p>
      <p class="drinks">Fizz Cola, Diet Fizz, Koala Cola, Diet Koala, Peak Dew, Diet Peak, Lemonade, Lime Up, Dr Pebble</p>
    </div>
  </section>

  <section class="menu-col kids">
    <h2 class="col-head small">SEASHELL<br>FINDERS<br>(KIDS)</h2>
    <div class="items list">
      <p class="item-name">Little Cheeseburger</p>
      <p class="item-name">Pulled Pork Sandwich</p>
      <p class="item-name">Mini Corn Dogs</p>
      <p class="item-name">Chicken Salad Sandwich</p>
      <p class="item-name">Fries/Onion Rings</p>
    </div>
  </section>

  <section class="menu-col sides">
    <h2 class="col-head">SIDES</h2>
    <div class="items list">
      <p class="item-name">Seasoned Fries</p>
      <p class="item-name">Onion Rings</p>
      <p class="item-name">Sweet Cornbread</p>
      <p class="item-name">Sweet Coleslaw</p>
      <p class="item-name">Macoroni Salad</p>
      <p class="item-name">Side Salad</p>
    </div>
  </section>

  <div class="brand"><span class="brand-dot"></span><span class="brand-name">Sandy Cove</span></div>
</main>
</body>
</html>
```